Graphics for a 'Shade Hunt' mobile phone project

I need the graphics (including source graphics in Illustrator or Photoshop) for the screens inside the game.

Please read the attached brief carefully, thanks!

```html
<!DOCTYPE html>
<html lang="en">
<head>
<meta charset="utf-8">
<title>Shade Hunt – Level Select</title>
<link rel="stylesheet" href="https://fonts.googleapis.com/css2?family=Montserrat:wght@700;800&family=Lora:wght@500&display=swap">
<style>
  :root {
    --header-top: #2bb6ee;
    --header-bottom: #0f8fcb;
    --header-line: #e6f6fc;
    --bg-center: #f4f8f8;
    --bg-edge: #bfe3e9;
    --white: #ffffff;
    --red: #e9202d;
    --red-dark: #c4111d;
    --magenta: #f02aa6;
    --magenta-dark: #c0167f;
    --purple: #8b3df0;
    --purple-dark: #5f1fc0;
    --blue: #25b2ec;
    --blue-dark: #0d86bf;
    --green: #3ce352;
    --green-dark: #1bb130;
    --lime: #d8ee22;
    --lime-dark: #a7c012;
    --orange: #ff9e26;
    --orange-dark: #d4760c;
    --ad-bg: #8e1414;
    --ad-bg-dark: #5e0b0b;
    --ad-gold: #f2cf8a;
    --ad-strip: #4a0808;
    --ad-badge: #f07a1a;
  }
  * { box-sizing: border-box; margin: 0; padding: 0; }
  html, body { width: 719px; height: 1200px; overflow: hidden; background: #fff; }
  body { font-family: "Montserrat", sans-serif; }

  .screen {
    position: relative; width: 719px; height: 1200px; overflow: hidden;
    background: radial-gradient(ellipse at 50% 45%, var(--bg-center) 0%, #e2f0f2 50%, var(--bg-edge) 100%);
  }

  .app-header {
    position: absolute; left: 0; top: 0; width: 719px; height: 114px;
    background: linear-gradient(var(--header-top), var(--header-bottom));
    border-bottom: 3px solid var(--header-line);
  }
  .back-button { position: absolute; left: 38px; top: 34px; width: 90px; height: 46px; }
  .app-name {
    position: absolute; left: 0; right: 0; top: 36px; text-align: center;
    color: var(--white); font-weight: 800; font-size: 34px; letter-spacing: 1px;
    text-transform: uppercase;
  }

  .level-list { position: absolute; left: 44px; top: 147px; width: 632px; list-style: none; }
  .level {
    position: relative; height: 97px; margin-bottom: 16px;
    border-radius: 49px; border: 4px solid var(--white);
    box-shadow: 0 4px 6px rgba(0,0,0,0.22);
    color: var(--white);
  }
  .level-title {
    position: absolute; left: 38px; top: 10px;
    font-size: 50px; font-weight: 700; line-height: 1;
    text-shadow: 0 2px 2px rgba(0,0,0,0.25);
  }
  .level--open .level-title { top: 18px; font-size: 54px; }
  .level-hint {
    position: absolute; left: 40px; top: 62px;
    font-size: 17px; font-weight: 700;
    text-shadow: 0 1px 1px rgba(0,0,0,0.3);
  }
  .level-icon { position: absolute; right: 32px; top: 26px; width: 38px; height: 40px; }

  .level--red { background: linear-gradient(var(--red), var(--red-dark)); }
  .level--magenta { background: linear-gradient(var(--magenta), var(--magenta-dark)); }
  .level--purple { background: linear-gradient(var(--purple), var(--purple-dark)); }
  .level--blue { background: linear-gradient(var(--blue), var(--blue-dark)); }
  .level--green { background: linear-gradient(var(--green), var(--green-dark)); }
  .level--lime { background: linear-gradient(var(--lime), var(--lime-dark)); }
  .level--orange { background: linear-gradient(var(--orange), var(--orange-dark)); }

  .ad-banner {
    position: absolute; left: 0; top: 1082px; width: 719px; height: 118px;
    background: linear-gradient(90deg, var(--ad-bg-dark), var(--ad-bg) 40%, var(--ad-bg-dark));
  }
  .ad-cta {
    position: absolute; left: 0; top: 0; width: 46px; height: 118px;
    background: var(--ad-strip); color: var(--white);
  }
  .ad-cta span {
    position: absolute; left: 50%; top: 50%; width: 118px;
    transform: translate(-50%, -50%) rotate(-90deg);
    font-family: "Lora", serif; font-size: 14px; line-height: 1.15; text-align: center;
  }
  .ad-art {
    position: absolute; left: 60px; top: 8px; width: 150px; height: 110px;
    background: linear-gradient(120deg, #f3ede2, #d9cdb8);
    border-radius: 8px 8px 0 0;
  }
  .ad-title {
    position: absolute; left: 226px; top: 24px;
    font-family: "Lora", serif; font-weight: 500; font-size: 60px; line-height: 1;
    color: var(--ad-gold);
  }
  .ad-badge {
    position: absolute; right: 8px; top: 8px; width: 26px; height: 26px;
    background: var(--ad-badge); border-radius: 50%;
  }
</style>
</head>
<body>
<main class="screen">
  <header class="app-header">
    <svg class="back-button" viewBox="0 0 90 46" aria-label="Back">
      <path d="M28 6 L6 23 L28 40 L28 29 L80 29 Q86 29 86 23 Q86 17 80 17 L28 17 Z" fill="#fff" stroke="#fff" stroke-width="4" stroke-linejoin="round"/>
    </svg>
    <h1 class="app-name">Shade Hunt</h1>
  </header>

  <ol class="level-list">
    <li class="level level--red level--open">
      <span class="level-title">Level 01</span>
      <svg class="level-icon" viewBox="0 0 38 40" aria-label="Play"><path d="M6 4 L34 20 L6 36 Z" fill="#fff" stroke="#fff" stroke-width="3" stroke-linejoin="round"/></svg>
    </li>
    <li class="level level--magenta">
      <span class="level-title">Level 02</span><span class="level-hint">Answer 16 images to unlock</span>
      <svg class="level-icon" viewBox="0 0 38 40" aria-label="Locked"><path d="M10 18 V12 a9 9 0 0 1 18 0 V18" fill="none" stroke="#fff" stroke-width="5"/><rect x="4" y="17" width="30" height="22" rx="4" fill="#fff"/></svg>
    </li>
    <li class="level level--purple">
      <span class="level-title">Level 03</span><span class="level-hint">Answer 16 images to unlock</span>
      <svg class="level-icon" viewBox="0 0 38 40" aria-label="Locked"><path d="M10 18 V12 a9 9 0 0 1 18 0 V18" fill="none" stroke="#fff" stroke-width="5"/><rect x="4" y="17" width="30" height="22" rx="4" fill="#fff"/></svg>
    </li>
    <li class="level level--blue">
      <span class="level-title">Level 04</span><span class="level-hint">Answer 16 images to unlock</span>
      <svg class="level-icon" viewBox="0 0 38 40" aria-label="Locked"><path d="M10 18 V12 a9 9 0 0 1 18 0 V18" fill="none" stroke="#fff" stroke-width="5"/><rect x="4" y="17" width="30" height="22" rx="4" fill="#fff"/></svg>
    </li>
    <li class="level level--green">
      <span class="level-title">Level 05</span><span class="level-hint">Answer 16 images to unlock</span>
      <svg class="level-icon" viewBox="0 0 38 40" aria-label="Locked"><path d="M10 18 V12 a9 9 0 0 1 18 0 V18" fill="none" stroke="#fff" stroke-width="5"/><rect x="4" y="17" width="30" height="22" rx="4" fill="#fff"/></svg>
    </li>
    <li class="level level--lime">
      <span class="level-title">Level 06</span><span class="level-hint">Answer 16 images to unlock</span>
      <svg class="level-icon" viewBox="0 0 38 40" aria-label="Locked"><path d="M10 18 V12 a9 9 0 0 1 18 0 V18" fill="none" stroke="#fff" stroke-width="5"/><rect x="4" y="17" width="30" height="22" rx="4" fill="#fff"/></svg>
    </li>
    <li class="level level--orange">
      <span class="level-title">Level 07</span><span class="level-hint">Answer 16 images to unlock</span>
      <svg class="level-icon" viewBox="0 0 38 40" aria-label="Locked"><path d="M10 18 V12 a9 9 0 0 1 18 0 V18" fill="none" stroke="#fff" stroke-width="5"/><rect x="4" y="17" width="30" height="22" rx="4" fill="#fff"/></svg>
    </li>
    <li class="level level--red">
      <span class="level-title">Level 08</span><span class="level-hint">Answer 16 images to unlock</span>
      <svg class="level-icon" viewBox="0 0 38 40" aria-label="Locked"><path d="M10 18 V12 a9 9 0 0 1 18 0 V18" fill="none" stroke="#fff" stroke-width="5"/><rect x="4" y="17" width="30" height="22" rx="4" fill="#fff"/></svg>
    </li>
  </ol>

  <aside class="ad-banner">
    <div class="ad-cta"><span>Touch to<br>play for FREE</span></div>
    <div class="ad-art" role="img" aria-label="Illustration of two playing cards for the card game"></div>
    <p class="ad-title">Web Patience</p>
    <span class="ad-badge"></span>
  </aside>
</main>
</body>
</html>
```